Movie Showtimes Website needs an updated new look

Website = www.marlovista.com

We want to update the look of our website. We want our website to look modern, trendy, something that was designed in 2018.

We don't need any HTML or CSS or web development. All we need is the graphical prototype, preferably in Photoshop with layers.

Most of our visitors use mobile devices. Our website is RESPONSIVE -- it is flexible to fit all screen sizes.

We will use this new logo (designed on Quillbarn):
https://www.quillbarn.com/design/27364512

Thank you for your kind consideration.

Please find attached 3 PDF files with the current webpages:

1. Each city location has its own HOME PAGE like this:

https://www.marlovista.com/ont/ottawa/

2. The most visited pages have movie SHOWTIMES and look like this:

https://www.marlovista.com/theatres/rovenna-hartfield-vip

MOVIE TITLE (poster + basic info + 4 buttons)
-- the type of the screening (ex. Regular, VYRA, 3D, etc.)
-- individual days and showtimes

3. INFORMATION about movies:

https://www.marlovista.com/movies/silent-copper-road-2018

Thank you.

Target Market(s)

Canada and USA, target audience = ages 13-50

Industry/Entity Type

Movie

Number of Pages Required

3 page

Font styles to use
Sans Serif

Colors

Designer to choose colors to be used in the design.

Requirements
Must have
• - For the main body text (such as movie times, description, information) we prefer dark text on a light background.
• - We will use the new logo https://www.quillbarn.com/design/27364512 -- but the text Marlo Vista in the logo doesn't have to look exactly like that, it can be on the same line and have the same or different size
Should not have
• No more than 2 different fonts (ex. one font for headers and titles, another one for text)

```html
<!DOCTYPE html>
<html lang="en">
<head>
<meta charset="utf-8">
<title>Marlo Vista — Movie Showtimes</title>
<link rel="stylesheet" href="https://fonts.googleapis.com/css2?family=Aleo:ital,wght@0,400;0,700;1,400&family=Lato:wght@400;700;900&display=swap">
<style>
:root{
  --ink:#111111;
  --topbar:#0d1220;
  --nav:#3d3d3d;
  --accent-red:#d5261f;
  --band-red:#c94a30;
  --pink:#ec0c6a;
  --blue:#3fa9e8;
  --orange:#f07d10;
  --gold:#f2c21b;
  --footer:#1c1c1c;
  --footer-text:#cfcfcf;
  --light:#ededed;
  --muted:#6b6b6b;
  --head:"Aleo", Georgia, serif;
  --body:"Lato", Arial, sans-serif;
}
*{box-sizing:border-box;margin:0;padding:0}
html,body{width:1200px;height:2748px;overflow:hidden}
body{position:relative;background:#fff;font-family:var(--body);color:var(--ink)}
.abs{position:absolute}

/* top strip */
.visitor-strip{left:0;top:0;width:1200px;height:33px;background:var(--topbar);color:#fff;font-size:11px;font-weight:700;display:flex;align-items:center;justify-content:center;gap:8px}
.visitor-strip .dot{width:14px;height:14px;border-radius:50%;background:#7b8bb0}

/* header */
.brand{display:flex;align-items:center;gap:10px}
.brand-mark{width:40px;height:40px;border-radius:50%;background:#2a2a2a}
.brand-name{font-family:var(--body);font-weight:900;font-size:22px;color:#2a2a2a;letter-spacing:.5px}
.header-brand{left:216px;top:51px}
.account{top:38px;display:flex;align-items:center;gap:7px;font-size:10px;font-weight:700}
.account .icon{width:13px;height:13px;border-radius:50%;background:#555}

/* navigation */
.main-nav{left:0;top:114px;width:1200px;height:54px;background:var(--nav);border-top:3px solid #2a2a2a;border-bottom:3px solid var(--accent-red)}
.main-nav a{position:absolute;top:14px;color:#fff;text-decoration:none;font-weight:700;font-size:16px}

/* hero */
.hero{left:101px;top:207px;width:998px;height:445px;border-radius:12px;overflow:hidden;background:radial-gradient(ellipse at 72% 45%,#e8c38a 0%,#a8642a 22%,#4a2a14 50%,#1c1410 80%);box-shadow:0 4px 10px rgba(0,0,0,.35)}
.hero-title{left:124px;top:140px;font-family:var(--head);font-weight:700;font-size:32px;color:#fff}
.hero-text{left:124px;top:180px;width:390px;font-family:var(--head);font-weight:700;font-size:16px;line-height:19px;color:#fff}
.hero-genres{left:124px;top:236px;font-family:var(--head);font-style:italic;font-size:19px;color:#fff;word-spacing:6px}
.play-btn{left:124px;top:273px;width:118px;height:32px;border:2px solid #fff;border-radius:16px;display:flex;align-items:center;gap:8px;padding-left:6px;color:#fff;font-family:var(--head);font-weight:700;font-size:15px}
.hero-dots{left:126px;top:414px;display:flex;gap:5px}
.hero-dots span{width:12px;height:12px;border:2px solid #fff;border-radius:50%}

/* tabs + search */
.tab{top:692px;height:41px;border:1px solid #cfcfcf;border-bottom:none;font-family:var(--head);font-size:15px;display:flex;align-items:center;justify-content:center;background:#fff;color:#333}
.tab.active{background:var(--band-red);color:#fff;border-color:var(--band-red)}
.quick-search{left:674px;top:698px;width:312px;height:29px;border:1px solid #d0d0d0;border-radius:15px;background:#fff}
.quick-search .select{position:absolute;left:-1px;top:-1px;width:62px;height:29px;border-radius:15px;background:#3b3b3b;color:#fff;font-size:9px;display:flex;align-items:center;justify-content:center}
.quick-search .go{position:absolute;right:-1px;top:-1px;width:64px;height:29px;border-radius:15px;background:var(--blue);color:#fff;font-size:9px;display:flex;align-items:center;justify-content:center}

.section-band{left:0;top:733px;width:1200px;height:75px;background:var(--band-red)}
.section-band h2{position:absolute;left:253px;top:17px;font-family:var(--head);font-weight:700;font-size:35px;color:#fff}
.view-toggle{position:absolute;left:896px;top:25px}

/* movie cards */
.movie{left:256px;width:700px;height:250px}
.poster{position:absolute;left:0;top:0;width:204px;height:249px;box-shadow:3px 5px 8px rgba(0,0,0,.35)}
.movie-title{position:absolute;left:231px;top:0;font-family:var(--head);font-weight:700;font-size:31px;line-height:34px}
.movie-genre{position:absolute;left:231px;top:35px;font-family:var(--head);font-size:18px}
.rating{position:absolute;left:231px;top:55px;font-family:var(--head);font-size:15px;display:flex;gap:8px;align-items:center}
.stars{color:var(--gold);font-size:14px;letter-spacing:1px}
.facts{position:absolute;left:231px;top:90px;font-family:var(--head);font-style:italic;font-size:18px;line-height:18.7px;color:#333}
.facts dt{float:left;clear:left;width:105px}
.facts dd{margin-left:105px}
.share{display:flex;gap:9px;padding-top:3px}
.share i{display:block;width:11px;height:11px;border-radius:50%}
.actions{position:absolute;left:231px;top:211px;display:flex;gap:9px}
.actions span{height:37px;border:2px solid var(--pink);border-radius:19px;display:flex;align-items:center;justify-content:center;font-family:var(--head);font-weight:700;font-size:15px;color:#222}
.actions .primary{background:var(--pink);color:#fff}

/* city finder */
.city-finder{left:0;top:1823px;width:1200px;height:216px;background:linear-gradient(180deg,#f3f4f6 0%,#e2e5ea 45%,#b7bfc9 72%,#8e99a5 85%,#dfe3e8 100%)}
.city-kicker{left:104px;top:1889px;font-family:var(--head);font-size:17px;color:#222}
.city-title{left:104px;top:1909px;font-family:var(--head);font-weight:700;font-size:38px;color:var(--orange)}
.city-search{left:377px;top:1891px;width:603px;height:29px;border:1px solid #cfcfcf;border-radius:15px;background:#fff;font-size:10px;color:#999;padding:8px 14px}
.city-go{left:991px;top:1891px;width:31px;height:31px;border-radius:50%;background:var(--orange);color:#fff;font-size:12px;font-weight:700;display:flex;align-items:center;justify-content:center}

/* coming soon */
.coming-bar{left:0;top:2039px;width:1200px;height:71px;background:var(--light)}
.coming-bar h3{position:absolute;left:218px;top:24px;font-family:var(--head);font-weight:700;font-size:19px}
.coming-link{position:absolute;left:779px;top:24px;font-family:var(--head);font-size:19px;color:#555;display:flex;align-items:center;gap:8px}
.coming-link .arrow{width:19px;height:19px;border-radius:50%;background:#888;display:flex;align-items:center;justify-content:center}
.soon{top:2136px;width:137px}
.soon .art{width:137px;height:194px}
.soon p{margin-top:10px;text-align:center;font-size:10px;font-weight:700}

/* footer */
.site-footer{left:0;top:2393px;width:1200px;height:355px;background:var(--footer);border-top:4px solid var(--accent-red)}
.schedule-btn{left:474px;top:2369px;width:250px;height:55px;border-radius:28px;background:var(--accent-red);color:#fff;font-weight:900;font-size:14px;display:flex;align-items:center;justify-content:center;letter-spacing:.5px}
.footer-brand{left:218px;top:2427px}
.footer-brand .brand-mark{background:#7a7a7a}
.footer-brand .brand-name{color:#8a8a8a}
.footer-col{top:2472px;color:var(--footer-text);font-size:9px;line-height:23.3px}
.footer-col h4{font-size:10px;font-weight:900;color:#fff;margin-bottom:13px;line-height:14px}
.footer-col ul{list-style:none}
.newsletter p{width:235px;line-height:20px;color:#bdbdbd}
.news-input{margin-top:8px;width:229px;height:31px;border:1px solid #4a4a4a;background:#2b2b2b;font-size:8px;color:#999;padding:9px 10px;line-height:12px}
.news-submit{margin-top:13px;width:86px;height:31px;border-radius:16px;background:var(--accent-red);color:#fff;font-weight:900;font-size:9px;display:flex;align-items:center;justify-content:center}
.socials{left:575px;top:2628px;display:flex;gap:15px}
.socials span{width:24px;height:24px;border-radius:50%;background:#fff}
.footer-rule{left:218px;top:2699px;width:764px;height:1px;background:#3a3a3a}
.legal{top:2718px;font-size:9px;color:#bdbdbd}
</style>
</head>
<body>

<div class="abs visitor-strip"><span class="dot"></span>Daily Visitors 32155</div>

<header>
  <div class="abs brand header-brand"><span class="brand-mark"></span><span class="brand-name">Marlo Vista</span></div>
  <div class="abs account" style="left:848px"><span class="icon"></span>Register</div>
  <div class="abs account" style="left:930px"><span class="icon" style="background:#8aa"></span>Login</div>
</header>

<nav class="abs main-nav">
  <svg class="abs" style="left:262px;top:12px" width="26" height="24" viewBox="0 0 26 24" aria-label="Home">
    <path d="M13 2 L25 12 H21 V23 H15 V16 H11 V23 H5 V12 H1 Z" fill="#3fa9e8"/>
  </svg>
  <a style="left:331px">Cinemas</a>
  <a style="left:431px">Movies</a>
  <a style="left:521px">Top 10</a>
  <a style="left:608px">Trailers</a>
  <a style="left:700px">Upcoming</a>
  <a style="left:813px">DVD</a>
  <a style="left:903px">More</a>
</nav>

<section class="abs hero">
  <div role="img" aria-label="Hero still: armed figures with bright flashlights in a dark, smoky interior" style="position:absolute;inset:0"></div>
  <h1 class="abs hero-title">End Of The World : Part-2</h1>
  <p class="abs hero-text">Lorem ipsum dolor sit amet, consectetur adipiscing elit. Donec rhoncus nulla erat, eget tempor purus sodales in.</p>
  <p class="abs hero-genres">Action, Adventure, Fantacy</p>
  <div class="abs play-btn">
    <svg width="20" height="20" viewBox="0 0 20 20"><circle cx="10" cy="10" r="8.5" fill="none" stroke="#fff" stroke-width="2"/><path d="M8 6 L14 10 L8 14 Z" fill="#fff"/></svg>
    Play Trial
  </div>
  <div class="abs hero-dots"><span></span><span></span><span></span></div>
</section>

<div class="abs tab active" style="left:224px;width:128px">Movies</div>
<div class="abs tab" style="left:354px;width:113px">Top 10</div>
<div class="abs tab" style="left:473px;width:119px">Upcoming</div>
<div class="abs quick-search"><span class="select">Movie ⌄</span><span class="go">Search</span></div>

<section class="abs section-band">
  <h2>New Movies This Week</h2>
  <svg class="view-toggle" width="48" height="24" viewBox="0 0 48 24" aria-label="Grid and list view">
    <rect x="0" y="2" width="9" height="9" fill="#fff"/><rect x="11" y="2" width="9" height="9" fill="#fff"/>
    <rect x="0" y="13" width="9" height="9" fill="#fff"/><rect x="11" y="13" width="9" height="9" fill="#fff"/>
    <rect x="26" y="2" width="5" height="5" fill="#fff"/><rect x="33" y="2" width="15" height="5" fill="#fff"/>
    <rect x="26" y="9.5" width="5" height="5" fill="#fff"/><rect x="33" y="9.5" width="15" height="5" fill="#fff"/>
    <rect x="26" y="17" width="5" height="5" fill="#fff"/><rect x="33" y="17" width="15" height="5" fill="#fff"/>
  </svg>
</section>

<article class="abs movie" style="top:837px">
  <div class="poster" role="img" aria-label="Movie poster for A Hollow Quiet" style="background:linear-gradient(180deg,#3a3029,#6b574a 50%,#1e1915)"></div>
  <h3 class="movie-title">A Hollow Quiet</h3>
  <p class="movie-genre">Horror/thriller</p>
  <div class="rating"><span class="stars">★★★★★</span>8.1 Rating</div>
  <dl class="facts">
    <dt>Year</dt><dd>2018</dd>
    <dt>Run time</dt><dd>1h30m</dd>
    <dt>Genre</dt><dd>Horror/thriller</dd>
    <dt>Directed by</dt><dd>Elias Varnholt</dd>
    <dt>Company</dt><dd>Brightvale Pictures</dd>
    <dt>Share</dt><dd><div class="share"><i style="background:#3b5998"></i><i style="background:#1da1f2"></i><i style="background:#8a5a44"></i><i style="background:#e60023"></i><i style="background:#1ab7ea"></i></div></dd>
  </dl>
  <div class="actions"><span class="primary" style="width:101px">Times</span><span style="width:106px">Info</span><span style="width:106px">Videos</span><span style="width:108px">Reviews</span></div>
</article>

<article class="abs movie" style="top:1172px">
  <div class="poster" role="img" aria-label="Movie poster for Curfew Crashers" style="background:linear-gradient(180deg,#121212 0%,#1a1a1a 40%,#c78a5a 70%,#7a4a30)"></div>
  <h3 class="movie-title">Curfew Crashers</h3>
  <p class="movie-genre">Comedy</p>
  <div class="rating"><span class="stars">★★★★★</span>7.3 Rating</div>
  <dl class="facts">
    <dt>Year</dt><dd>2018</dd>
    <dt>Run time</dt><dd>1h42m</dd>
    <dt>Genre</dt><dd>Comedy</dd>
    <dt>Directed by</dt><dd>Mira Tolland</dd>
    <dt>Company</dt><dd>Orrin Gate Pictures</dd>
    <dt>Share</dt><dd><div class="share"><i style="background:#3b5998"></i><i style="background:#1da1f2"></i><i style="background:#8a5a44"></i><i style="background:#e60023"></i><i style="background:#1ab7ea"></i></div></dd>
  </dl>
  <div class="actions"><span class="primary" style="width:101px">Times</span><span style="width:106px">Info</span><span style="width:106px">Videos</span><span style="width:108px">Reviews</span></div>
</article>

<article class="abs movie" style="top:1517px">
  <div class="poster" role="img" aria-label="Movie poster for The Rally Season" style="background:linear-gradient(135deg,#e7b9a4,#f3e6ec 45%,#8fb6d6 80%,#6a8fb0)"></div>
  <h3 class="movie-title">The Rally Season</h3>
  <p class="movie-genre">Drama</p>
  <div class="rating"><span class="stars">★★★★★</span>7.4 Rating</div>
  <dl class="facts">
    <dt>Year</dt><dd>2018</dd>
    <dt>Run time</dt><dd>1h41m</dd>
    <dt>Genre</dt><dd>Drama</dd>
    <dt>Directed by</dt><dd>Dorian Welke</dd>
    <dt>Company</dt><dd>Halverd Pictures</dd>
    <dt>Share</dt><dd><div class="share"><i style="background:#3b5998"></i><i style="background:#1da1f2"></i><i style="background:#8a5a44"></i><i style="background:#e60023"></i><i style="background:#1ab7ea"></i></div></dd>
  </dl>
  <div class="actions"><span class="primary" style="width:101px">Times</span><span style="width:106px">Info</span><span style="width:106px">Videos</span><span style="width:108px">Reviews</span></div>
</article>

<section class="abs city-finder" role="img" aria-label="Misty mountain landscape background"></section>
<p class="abs city-kicker">Movie To Watch Now</p>
<p class="abs city-title">IN YOUR CITY</p>
<div class="abs city-search">Movie search...</div>
<div class="abs city-go">Go</div>

<section class="abs coming-bar">
  <h3>COMING SOON</h3>
  <div class="coming-link">Movies Coming Soon
    <span class="arrow"><svg width="9" height="9" viewBox="0 0 9 9"><path d="M2 1 L7 4.5 L2 8" fill="none" stroke="#fff" stroke-width="2"/></svg></span>
  </div>
</section>

<div class="abs soon" style="left:145px"><div class="art" role="img" aria-label="Poster for Always Your Summer" style="background:linear-gradient(180deg,#f4c07a,#c98a52 60%,#6e4a30)"></div><p>Always Your Summer</p></div>
<div class="abs soon" style="left:300px"><div class="art" role="img" aria-label="Poster for Titans : Endgame Dawn" style="background:linear-gradient(180deg,#2a2f4a,#7a3a44 55%,#1a1c2a)"></div><p>Titans : Endgame Dawn</p></div>
<div class="abs soon" style="left:456px"><div class="art" role="img" aria-label="Poster for Bandolero" style="background:linear-gradient(180deg,#f4d22a,#e6a020 55%,#3a7a3a)"></div><p>Bandolero</p></div>
<div class="abs soon" style="left:610px"><div class="art" role="img" aria-label="Poster for Stampede" style="background:linear-gradient(180deg,#9fb2c0,#5a6a78 55%,#2a2e33)"></div><p>Stampede</p></div>
<div class="abs soon" style="left:766px"><div class="art" role="img" aria-label="Poster for Velvet Grudge" style="background:linear-gradient(180deg,#1a1414,#3a2622 55%,#120e0e)"></div><p>Velvet Grudge</p></div>
<div class="abs soon" style="left:920px"><div class="art" role="img" aria-label="Poster for Dear Theo" style="background:linear-gradient(180deg,#e23a3a,#c92a36 55%,#3a4a6a)"></div><p>Dear Theo</p></div>

<footer class="abs site-footer"></footer>
<div class="abs schedule-btn">MOVIE SCHEDULE</div>
<div class="abs brand footer-brand"><span class="brand-mark"></span><span class="brand-name">Marlo Vista</span></div>

<div class="abs footer-col" style="left:295px">
  <h4>HOME</h4>
  <ul><li>Cinemas</li><li>Movies</li><li>Top 10</li><li>Trailers</li><li>Upcoming</li><li>DVD</li></ul>
</div>
<div class="abs footer-col" style="left:423px">
  <h4>ABOUT</h4>
  <ul><li>My Favourite Cinemas</li><li>My Movie Library</li><li>Gala Awards</li><li>Promotions</li><li>Change Location</li><li>Contact Us</li></ul>
</div>
<div class="abs footer-col" style="left:575px">
  <h4>CONTACT US</h4>
  <ul><li>Marlo Vista</li><li>d.b.a Tallowmark</li><li>418 Larkfield Avenue</li><li>Suite 210</li><li>Brenmoor, DE 19877</li></ul>
</div>
<div class="abs footer-col newsletter" style="left:751px">
  <h4>SUBSCRIBE TO OUR NEWSLETTER</h4>
  <p>Subscribe to our newsletter to stay up to date with the latest news.</p>
  <div class="news-input">Enter your email address</div>
  <div class="news-submit">SUBMIT</div>
</div>
<div class="abs socials"><span></span><span></span><span></span><span></span></div>

<div class="abs footer-rule"></div>
<p class="abs legal" style="left:218px">Copyright © 2016 &nbsp;&nbsp; All Rights Reserved</p>
<p class="abs legal" style="left:841px">Terms of Use &nbsp;&nbsp;|&nbsp;&nbsp; Privacy Policy</p>

</body>
</html>
```